Rebrand stationary with recently completed logo design

Need new business cards, thank you cards, letterhead, envelopes and presentation folders. The designs will be sent to a separate production firm so I need the files to be print ready.

My contact info
Reno Vaskelind

Office 604-381-4756
Fax 604-318-5064

Email reno@glazeworks.ca
website www.glazeworks.ca

315-27140 62nd Avenue,
Langley, BC, V3K 2R8

Target Market(s)

Homeowners, businesses and contractors

Industry/Entity Type

Business

Font styles to use
Sans Serif

Colors
34a7d7

Requirements
Must have
• Like to have one side of the business card a solid color with the logo in all white. The side with all the text to be a white background
• I find the current blue on the front of the card with the white logo too dark.
Should not have
• Gradient colors

```html
<!DOCTYPE html>
<html lang="en">
<head>
<meta charset="utf-8">
<title>GlazeWorks Business Card</title>
<link href="https://fonts.googleapis.com/css2?family=Open+Sans:wght@400;600&family=Roboto+Condensed:wght@700&display=swap" rel="stylesheet">
<style>
  :root {
    --backdrop: #dedad5;
    --card-white: #f7f7f6;
    --slate: #3d4b55;
    --brand-blue: #1b8dd4;
    --text-grey: #4f565c;
    --rule-grey: #8a8f93;
    --white: #ffffff;
  }
  * { margin: 0; padding: 0; box-sizing: border-box; }
  html, body {
    width: 1200px; height: 960px; overflow: hidden;
    background: var(--backdrop);
    font-family: "Open Sans", sans-serif;
  }
  .stage { position: relative; width: 1200px; height: 960px; }
  .card {
    position: absolute; width: 600px; height: 342px;
    box-shadow: 0 3px 8px rgba(0,0,0,0.25);
  }
  .card-front { left: 302px; top: 130px; background: var(--card-white); }
  .card-back { left: 299px; top: 488px; background: var(--slate); }

  .wordmark {
    position: absolute; display: flex; align-items: center;
    font-family: "Open Sans", sans-serif; font-weight: 400;
    letter-spacing: 0.5px; white-space: nowrap;
  }
  .wordmark-square { display: block; }
  .card-front .wordmark {
    left: 0; right: 0; top: 140px; justify-content: center;
    font-size: 38px; color: var(--slate); gap: 14px;
  }
  .card-front .wordmark-square { width: 26px; height: 26px; background: var(--slate); }
  .card-back .wordmark {
    left: 0; right: 0; top: 138px; justify-content: center;
    font-size: 44px; color: var(--white); gap: 18px;
  }
  .card-back .wordmark-square { width: 34px; height: 34px; background: var(--white); }

  .name-rule {
    position: absolute; left: 55px; top: 222px; width: 491px; height: 26px;
    display: flex; align-items: center; gap: 4px;
  }
  .name-rule::before, .name-rule::after {
    content: ""; flex: 1; height: 1px; background: var(--rule-grey);
  }
  .holder-name {
    font-family: "Roboto Condensed", sans-serif; font-weight: 700;
    font-size: 19px; color: var(--brand-blue); letter-spacing: 0.2px;
  }

  .contact-row {
    position: absolute; top: 266px; left: 0; width: 600px; height: 40px;
    font-size: 13px; line-height: 19px; color: var(--text-grey);
  }
  .contact-block { position: absolute; top: 0; }
  .address { right: 393px; text-align: right; }
  .divider { position: absolute; top: 2px; width: 1px; height: 34px; background: var(--rule-grey); }
  .divider-one { left: 226px; }
  .divider-two { left: 375px; }
  .phones { left: 244px; }
  .web { left: 395px; }
  .line { display: flex; align-items: center; gap: 8px; }
  .line svg { width: 14px; height: 14px; flex: none; fill: var(--brand-blue); }
</style>
</head>
<body>
<main class="stage">
  <section class="card card-front" aria-label="Business card front">
    <div class="wordmark"><span class="wordmark-square"></span>GlazeWorks</div>
    <div class="name-rule"><span class="holder-name">RENO VASKELIND</span></div>
    <div class="contact-row">
      <div class="contact-block address">
        <div>315-27140 62nd Avenue</div>
        <div>Langley, BC, V3K 2R8</div>
      </div>
      <span class="divider divider-one"></span>
      <div class="contact-block phones">
        <div class="line">
          <svg viewBox="0 0 16 16" aria-hidden="true"><path d="M3.6 1.2l2.2 2.6c.3.4.3.9 0 1.3L4.7 6.3c.8 1.9 2.3 3.4 4.2 4.3l1.2-1.1c.4-.3.9-.3 1.3 0l2.5 2.2c.4.4.4 1 0 1.4l-1.3 1.3c-.6.6-1.5.8-2.3.5C6.3 13.4 2.6 9.7 1.1 5.6.8 4.8 1 3.9 1.6 3.3l1.3-1.2c.3-.3.5-.3.7-.9z"/></svg>
          <span>604-381-4756</span>
        </div>
        <div class="line">
          <svg viewBox="0 0 16 16" aria-hidden="true"><path d="M4 1h7l1 1v3H4z M1.5 6h13c.6 0 1 .4 1 1v5h-3v-2h-9v2h-3V7c0-.6.4-1 1-1z M4.5 11h7v4h-7z"/></svg>
          <span>604-318-5064</span>
        </div>
      </div>
      <span class="divider divider-two"></span>
      <div class="contact-block web">
        <div class="line">
          <svg viewBox="0 0 16 16" aria-hidden="true"><path d="M1 3h14v1.2L8 8.6 1 4.2z M1 5.6l7 4.4 7-4.4V13H1z"/></svg>
          <span>reno@glazeworks.ca</span>
        </div>
        <div class="line">
          <svg viewBox="0 0 16 16" aria-hidden="true"><path d="M8 1a7 7 0 1 0 0 14A7 7 0 0 0 8 1zm-1 2.2c-.6.8-1.4 1.2-1.2 2.2.2.9 1.5.7 1.8 1.6.3.8-.7 1.3-.4 2.2.3.8 1.3 1.1 1.3 2.1 0 .8-.5 1.5-1 2.1A5.3 5.3 0 0 1 3.1 6.4C4 4.6 5.3 3.5 7 3.2zm3.5.8c1.6.9 2.7 2.6 2.8 4.6-.8-.2-1.4-.8-2.1-.5-.7.3-.5 1.4-1.2 1.6-.7.2-1.3-.6-1.2-1.4.1-.9 1-1.4 1.1-2.3.1-.7-.3-1.3.6-2z"/></svg>
          <span>www.glazeworks.ca</span>
        </div>
      </div>
    </div>
  </section>

  <section class="card card-back" aria-label="Business card back">
    <div class="wordmark"><span class="wordmark-square"></span>GlazeWorks</div>
  </section>
</main>
</body>
</html>
```